Business Card Design for a Personal Trainer

I need a business card design for my job as a personal trainer. It should have a unique, modern and exclusive design. On the front there should be only my logo with my name and my job. 0163/2918374 Tobias Kellinger Lindenfeldweg 14 80412 Munich Germany The most important contact information is the web adress. it can be bigger than the rest, but its not necessary. The card should be 8,5cmx5,5cm big. Font: Roboto. Colors: black, white, gray, 56c1ff.

```html
<!DOCTYPE html>
<html lang="de">
<head>
<meta charset="utf-8">
<title>Tobias Kellinger – Personal Trainer Business Card</title>
<link href="https://fonts.googleapis.com/css2?family=Roboto:wght@300;400;500;700&display=swap" rel="stylesheet">
<style>
  :root {
    --stage: #2b2b2d;
    --card-black: #262626;
    --white: #ffffff;
    --gray-light: #d9d9dc;
    --gray-mid: #8a8a90;
    --accent: #56c1ff;
    --sky-deep: #1e2029;
    --sky-mid: #3b3d50;
    --sky-light: #6a6b80;
  }
  * { box-sizing: border-box; margin: 0; padding: 0; }
  html, body {
    width: 1200px; height: 1021px; overflow: hidden;
    background: var(--stage);
    font-family: "Roboto", Arial, sans-serif;
  }
  .stage { position: relative; width: 1200px; height: 1021px; }

  .card {
    position: absolute;
    width: 578px; height: 374px;
    border-radius: 4px;
    overflow: hidden;
    box-shadow: 0 18px 40px rgba(0,0,0,.45);
  }

  /* Front */
  .card--front {
    left: 450px; top: 90px;
    background: var(--card-black);
    display: flex; flex-direction: column; align-items: center; justify-content: center;
    color: var(--white);
  }
  .brand-name {
    font-weight: 400;
    font-size: 44px;
    letter-spacing: 2px;
    text-transform: uppercase;
    color: var(--white);
  }
  .brand-job {
    display: flex; align-items: center; gap: 12px;
    margin-top: 6px;
    font-size: 15px; font-weight: 400;
    letter-spacing: 6px;
    text-transform: uppercase;
    color: var(--white);
  }
  .brand-job::before, .brand-job::after {
    content: ""; width: 64px; height: 1px; background: var(--white);
  }

  /* Back */
  .card--back {
    left: 172px; top: 530px;
    background: linear-gradient(165deg, var(--sky-light) 0%, var(--sky-mid) 40%, var(--sky-deep) 100%);
  }
  .portrait {
    position: absolute; right: 0; top: 40px;
    width: 272px; height: 334px;
    background: linear-gradient(180deg, #8b8b92 0%, #55555c 45%, #3a3a3f 100%);
    border-radius: 110px 110px 0 0;
    opacity: .85;
  }
  .contact {
    position: absolute; left: 22px; top: 92px;
    width: 268px;
    text-align: center;
    color: var(--white);
  }
  .contact__web {
    font-weight: 700; font-size: 20px;
    color: var(--accent);
    margin-bottom: 16px;
    white-space: nowrap;
  }
  .contact__line { font-size: 17px; font-weight: 400; line-height: 1.3; }
  .contact__rule {
    width: 56px; height: 2px; background: var(--accent);
    margin: 16px auto 18px;
  }
</style>
</head>
<body>
<main class="stage">
  <section class="card card--front" aria-label="Business card front">
    <div class="brand-name">Tobias Kellinger</div>
    <div class="brand-job">Personal Trainer</div>
  </section>

  <section class="card card--back" aria-label="Business card back">
    <div class="portrait" role="img" aria-label="Black and white portrait of the trainer with arms crossed in a grey sports shirt"></div>
    <div class="contact">
      <p class="contact__web">www.tobiaskellinger.de</p>
      <p class="contact__line">0163/2918374</p>
      <p class="contact__line">t.kellinger@postfach.de</p>
      <div class="contact__rule"></div>
      <p class="contact__line">Lindenfeldweg 14</p>
      <p class="contact__line">80412 München</p>
    </div>
  </section>
</main>
</body>
</html>
```